Business Card Design

It's an investment advisory service for individuals with all there investment needs. Also financial consulting to businesses and governmental agencies on retirement plans etc. It's personalized not commoditized help. Should show strength, knowledge and money orientation.

Industry/Entity Type

Investment

Contact Information for Business Card

B. Vel R. Financial Consulting and Wealth Management, Mirek Dale Hopstein, 5172 Paseo Las Colinas Verde, San Diego, CA 92084-6617, Registered Investment Advisor

Requirements
Nice to have
• Something money oriented

```html
<!DOCTYPE html>
<html lang="en">
<head>
<meta charset="UTF-8">
<title>B Vel R – Business Card</title>
<link rel="stylesheet" href="https://fonts.googleapis.com/css2?family=Arimo:wght@400;700&family=Open+Sans:wght@400&display=swap">
<style>
  :root {
    --bg-center: #3a3a3a;
    --bg-edge: #000000;
    --gold: #e8bb4e;
    --gold-soft: #f0c75c;
    --band-light: #e6d497;
    --band-mid: #d8bc65;
    --band-dark: #c49a26;
    --band-edge: #f2e2a6;
    --ink: #121212;
    --dollar: #2f2f2f;
  }
  html, body {
    margin: 0;
    padding: 0;
    overflow: hidden;
    background: #000;
  }
  .card {
    position: relative;
    width: 1200px;
    height: 717px;
    overflow: hidden;
    background: radial-gradient(ellipse 620px 460px at 600px 250px, var(--bg-center) 0%, #1a1a1a 55%, var(--bg-edge) 100%);
    font-family: "Arimo", Arial, sans-serif;
  }
  .corner-dollar {
    position: absolute;
    font-family: "Arimo", Arial, sans-serif;
    font-weight: 700;
    font-size: 128px;
    line-height: 1;
    color: var(--dollar);
  }
  .corner-dollar.top-left { left: 24px; top: 22px; }
  .corner-dollar.top-right { left: 1102px; top: 22px; }
  .corner-dollar.bottom-left { left: 24px; top: 565px; }
  .corner-dollar.bottom-right { left: 1118px; top: 565px; }

  .brand-name {
    position: absolute;
    left: 0;
    width: 1200px;
    top: 38px;
    margin: 0;
    text-align: center;
    font-family: "Arimo", Arial, sans-serif;
    font-weight: 700;
    font-size: 92px;
    line-height: 1;
    color: var(--gold);
  }
  .tagline {
    position: absolute;
    left: 0;
    width: 1200px;
    top: 174px;
    margin: 0;
    text-align: center;
    font-family: "Arimo", Arial, sans-serif;
    font-size: 33px;
    color: var(--gold);
  }
  .name-band {
    position: absolute;
    left: 0;
    top: 295px;
    width: 1200px;
    height: 157px;
    box-sizing: border-box;
    border-top: 2px solid var(--band-edge);
    border-bottom: 2px solid var(--band-dark);
    background: linear-gradient(180deg, var(--band-light) 0%, var(--band-mid) 45%, var(--band-dark) 100%);
    display: flex;
    align-items: center;
    justify-content: center;
  }
  .person-name {
    margin: 0;
    font-family: "Arimo", Arial, sans-serif;
    font-weight: 700;
    font-size: 86px;
    letter-spacing: -0.5px;
    color: var(--ink);
    -webkit-text-stroke: 1.5px #000;
  }
  .person-title {
    position: absolute;
    left: 0;
    width: 1200px;
    top: 466px;
    margin: 0;
    text-align: center;
    font-family: "Open Sans", Arial, sans-serif;
    font-size: 26px;
    color: var(--gold);
  }
  .address {
    position: absolute;
    left: 0;
    width: 1200px;
    top: 623px;
    margin: 0;
    text-align: center;
    font-family: "Open Sans", Arial, sans-serif;
    font-size: 35px;
    color: var(--gold-soft);
  }
</style>
</head>
<body>
  <div class="card">
    <span class="corner-dollar top-left" aria-hidden="true">$</span>
    <span class="corner-dollar top-right" aria-hidden="true">$</span>
    <span class="corner-dollar bottom-left" aria-hidden="true">$</span>
    <span class="corner-dollar bottom-right" aria-hidden="true">$</span>

    <h1 class="brand-name">B Vel R</h1>
    <p class="tagline">Financial Consulting and Wealth Management</p>

    <div class="name-band">
      <h2 class="person-name">Mirek Dale Hopstein</h2>
    </div>

    <p class="person-title">Registered Investment Advisor</p>
    <p class="address">5172 Paseo Las Colinas Verde, San Diego, CA 92084-6617</p>
  </div>
</body>
</html>
```